Postcard Design

The business Logo is 'Swardley' it is grass cutting and maintenance. It will offer grass cutting with stripes including edging. Other services include decking/fencing maintenance, lawn treatment and patio/drive cleaning...... prices start from £10 to include front and rear lawns, Regular cuts or a one off tidy. private and commercial. Contracts welcome.
call 01642583106 or 07474829150 for a free quote.
one of the pics that i have sent is the logo (obviously it would need to be tidied up and neater) that is just rough. The other pic is one of pella cards templates but is the one that is the preferred out of all of them. If it could be similar to that with the logo on would be great.
a before (long scruffy grass) and after (neat Lawn) half and half of the postcard would be great.

Target Market(s)

Middle class home owners.

Industry/Entity Type

Business

Requirements
Must have
• The 'Swardley' logo
Nice to have
• we have a lot of junk mail posted in this area and a lot just gets put in the bin so could you make it eye catching.

```html
<!DOCTYPE html>
<html lang="en">
<head>
<meta charset="utf-8">
<title>Swardley – Lawn Service Postcard</title>
<link rel="stylesheet" href="https://fonts.googleapis.com/css2?family=Mulish:wght@600;700;800&display=swap">
<style>
  :root {
    --page: #ffffff;
    --lime: #8dc63f;
    --lime-soft: #a9d27a;
    --band: rgba(24, 52, 18, 0.82);
    --ink: #15200f;
    --white: #ffffff;
    --orange: #f7941d;
    --ribbon-top: #3a3f36;
    --ribbon-bottom: #121511;
  }
  * { margin: 0; padding: 0; box-sizing: border-box; }
  html, body { width: 1200px; height: 900px; overflow: hidden; background: var(--page); }
  body { position: relative; font-family: "Mulish", "Helvetica Neue", Arial, sans-serif; }

  .postcard {
    position: absolute; left: 35px; top: 12px; width: 1132px; height: 873px;
    overflow: hidden; box-shadow: 0 0 4px rgba(0,0,0,0.35);
  }
  .lawn-scene {
    position: absolute; inset: 0;
    background:
      radial-gradient(ellipse at 70% 8%, rgba(200,215,190,0.35), transparent 30%),
      linear-gradient(180deg, #2f5a22 0%, #3d6b2a 22%, #4f7e30 38%, #5e9a2e 46%, #6fb52c 58%, #7cc231 75%, #86c93a 100%);
  }
  .postcard > * { position: absolute; }

  .brand {
    left: 808px; top: 61px; width: 182px; height: 80px;
    background: var(--lime); border: 1px solid #5f8f2a;
    display: flex; align-items: center; justify-content: center;
    font-weight: 800; font-size: 30px; letter-spacing: 0.5px; color: var(--ink);
  }

  .headline {
    left: 152px; top: 197px; color: var(--white);
    font-weight: 800; font-size: 51px; line-height: 62px; letter-spacing: -0.3px;
    text-transform: uppercase;
  }
  .tagline {
    left: 152px; top: 388px; color: var(--white);
    font-weight: 700; font-size: 25px;
  }

  .info-band { left: 121px; top: 437px; width: 1011px; height: 198px; background: var(--band); }

  .services { left: 151px; top: 466px; color: var(--lime-soft); }
  .services-title { font-weight: 700; font-size: 23px; color: var(--lime); margin-bottom: 0; }
  .services-list { list-style: none; font-weight: 700; font-size: 22.5px; line-height: 27.5px; }
  .services-list li { display: flex; align-items: center; }
  .services-list li::before {
    content: ""; width: 13px; height: 13px; border-radius: 50%;
    background: #5e7f45; margin-right: 8px;
  }

  .quote-label { left: 708px; top: 472px; color: var(--white); font-weight: 700; font-size: 26px; }
  .phone-bar {
    left: 662px; top: 508px; width: 470px; height: 62px; background: var(--lime);
    display: flex; align-items: center; padding-left: 8px;
    font-weight: 800; font-size: 25.5px; color: var(--ink); letter-spacing: -0.3px;
  }
  .phone-bar svg { width: 34px; height: 42px; margin-right: 2px; }

  .price-ribbon { left: 151px; top: 657px; width: 275px; height: 106px; }
  .price-box {
    position: absolute; left: 0; top: 0; width: 275px; height: 63px;
    background: linear-gradient(180deg, var(--ribbon-top), var(--ribbon-bottom));
    color: var(--lime); font-weight: 800; font-size: 26px; line-height: 27px;
    text-align: center; padding-top: 5px; text-transform: uppercase;
  }
  .price-box .amount { color: var(--orange); }
  .price-ribbon svg { position: absolute; left: 0; top: 63px; }

  .price-note {
    left: 178px; top: 723px; width: 220px; text-align: center;
    color: var(--white); font-weight: 700; font-size: 19.5px; line-height: 23px;
  }
</style>
</head>
<body>
  <main class="postcard">
    <div class="lawn-scene" role="img" aria-label="Photo of a freshly striped green lawn with tall trees and houses behind"></div>

    <div class="brand">SWARDLEY</div>

    <h1 class="headline">The best<br>lawn service provider<br>in your area</h1>
    <p class="tagline">We accepted private and commercial contracts</p>

    <div class="info-band"></div>

    <section class="services">
      <h2 class="services-title">Services:</h2>
      <ul class="services-list">
        <li>Grass cutting and maintenance</li>
        <li>Decking/Fencing maintenance,</li>
        <li>Lawn treatment</li>
        <li>Patio/Drive cleaning</li>
      </ul>
    </section>

    <p class="quote-label">For Free Quotes:</p>
    <div class="phone-bar">
      <svg viewBox="0 0 24 30" aria-hidden="true">
        <path fill="#4a7226" d="M6 2c1.2-.6 2.3 0 2.8 1.2l1.6 4.2c.4 1-.1 2-1 2.5l-1.3.7c-.4.3-.6.8-.4 1.3 1 3.3 2.6 6.4 4.8 9 .3.4.9.5 1.3.2l1.2-.8c.9-.6 2-.4 2.6.5l2.6 3.6c.7 1 .4 2.2-.6 2.9l-1.6 1C14.5 31 6 22 3.2 12.6 2.3 9.4 2.4 6 3.8 3.4 4.3 2.8 5.1 2.4 6 2z"/>
      </svg>
      <span>0 164 258 3106 / 0 747 482 9150</span>
    </div>

    <div class="price-ribbon">
      <div class="price-box">Price starts<br>from <span class="amount">£10</span></div>
      <svg width="275" height="30" viewBox="0 0 275 30" aria-hidden="true">
        <polygon points="0,0 44,0 44,28 14,20" fill="#1a1d18"/>
        <polygon points="275,0 231,0 231,28 261,20" fill="#1a1d18"/>
      </svg>
    </div>
    <p class="price-note">include front and<br>rear lawns,<br>Regular cuts or<br>a one off tidy.</p>
  </main>
</body>
</html>
```